Business Card Design - ThriveMetric

Looking for creative, modern design, two sided for ThriveMetric that is consistent with color and feel of website www.thrivemetric.net.

Back of card will be used to promote products or have a quote revolving around decisions, change, leadership, innovation, creativity. Back should also have space to promote website, but optional to use the icon. Front of the card will need to use the icon and have standard place for name, job title, phone and email. We are not looking to put a mailing address or fax. Also want space to place a few words/phrase explaining what we do...such as individual growth and organizational development or tools, training, information...in addition, want the linkpage icon small on the front somewhere as we are also on linkpage.

Vector file uploaded of icon.

Target Market(s)

Professional coaching for individual growth and organizational development

Industry/Entity Type

Business

Requirements
Must have
• Icon...see attached.

```html
<!DOCTYPE html>
<html lang="en">
<head>
<meta charset="utf-8">
<title>ThriveMetric Business Card</title>
<link href="https://fonts.googleapis.com/css2?family=Arimo:wght@400;700&family=Saira+Semi+Condensed:wght@700&display=swap" rel="stylesheet">
<style>
  :root {
    --backdrop: #d9dbde;
    --card: #ffffff;
    --brand-blue: #1d86c6;
    --band-light: #8fd6f5;
    --band-dark: #1ba4e0;
    --ink: #2b2b2b;
    --muted: #555555;
    --name-ink: #3a3a3a;
    --edge: #9a9a9a;
  }
  html, body {
    margin: 0;
    width: 1200px;
    height: 1060px;
    overflow: hidden;
    background: var(--backdrop);
    font-family: "Arimo", Arial, sans-serif;
  }
  .card {
    position: absolute;
    background: var(--card);
    border: 1px solid var(--edge);
    box-sizing: border-box;
    overflow: hidden;
  }
  .card-front { left: 61px; top: 59px; width: 781px; height: 447px; }
  .card-back { left: 351px; top: 553px; width: 779px; height: 443px; }

  .brand-band {
    position: absolute; left: 0; top: 0; width: 118px; height: 100%;
    background: linear-gradient(90deg, var(--band-light), var(--band-dark));
  }
  .brand-band-rule {
    position: absolute; left: 118px; top: 0; width: 4px; height: 100%;
    background: var(--card);
  }
  .brand-band-rule::after {
    content: ""; position: absolute; left: 4px; top: 0; width: 2px; height: 100%;
    background: var(--band-dark);
  }
  .brand-mark {
    position: absolute; left: 22px; top: 55px; width: 130px; height: 130px;
    border-radius: 50%; background: var(--card);
  }
  .brand-name {
    position: absolute; left: 190px; top: 110px;
    font-size: 38px; font-weight: 700; color: var(--brand-blue);
    letter-spacing: 0.3px;
  }

  .contact-list {
    position: absolute; left: 140px; top: 256px; margin: 0; padding: 0; list-style: none;
    font-size: 20px; color: var(--ink);
  }
  .contact-list li { display: flex; align-items: center; height: 27px; }
  .contact-list svg { width: 13px; height: 13px; margin-right: 9px; flex: none; }
  .social-dot { width: 12px; height: 12px; background: #3b5da8; margin-right: 10px; flex: none; }

  .tagline {
    position: absolute; left: 140px; top: 378px; margin: 0;
    font-size: 20px; line-height: 26px; color: var(--ink);
  }
  .person {
    position: absolute; right: 50px; top: 254px; text-align: right;
  }
  .person-name {
    font-family: "Saira Semi Condensed", "Arial Narrow", sans-serif;
    font-size: 29px; font-weight: 700; color: var(--name-ink); line-height: 32px;
  }
  .person-title { font-size: 19px; color: var(--muted); margin-top: 2px; }

  .quote-list { position: absolute; left: 40px; top: 38px; margin: 0; padding: 0; list-style: none; }
  .quote { position: relative; height: 79px; padding-left: 70px; }
  .quote-dot {
    position: absolute; left: 3px; top: 4px; width: 30px; height: 30px; border-radius: 50%;
    background: radial-gradient(circle at 40% 40%, #e6f3fb, #3a9ad6);
  }
  .quote-text { font-size: 20px; color: var(--ink); line-height: 26px; }
  .quote-text::before, .quote-text::after {
    font-family: Georgia, serif; font-weight: 700; font-size: 34px; color: var(--ink);
    line-height: 0; position: relative;
  }
  .quote-text::before { content: "\201C"; position: absolute; left: 40px; top: 20px; }
  .quote-text::after { content: "\201D"; top: 18px; margin-left: 2px; }
  .quote-author { font-size: 20px; font-weight: 700; color: var(--brand-blue); margin-top: 2px; }
  .quote-author::before { content: "- "; color: var(--ink); font-weight: 400; }
</style>
</head>
<body>

<section class="card card-front" aria-label="Card front">
  <div class="brand-band"></div>
  <div class="brand-band-rule"></div>
  <div class="brand-mark"></div>
  <div class="brand-name">ThriveMetric</div>

  <ul class="contact-list">
    <li>
      <svg viewBox="0 0 12 12" aria-hidden="true"><path d="M2.5 1l2 2.3-1 1.2c.7 1.5 1.7 2.5 3 3.1l1.2-1 2.3 2-1.2 1.9C5 10.3 1.5 6.8.7 2.2z" fill="none" stroke="#333" stroke-width="1"/></svg>
      123-456-789
    </li>
    <li>
      <svg viewBox="0 0 12 12" aria-hidden="true"><rect x="0.5" y="2.5" width="11" height="7.5" fill="#333"/><path d="M0.5 2.5l5.5 4.5 5.5-4.5" fill="none" stroke="#fff" stroke-width="1"/></svg>
      info@thrivemetric.net
    </li>
    <li>
      <svg viewBox="0 0 12 12" aria-hidden="true"><circle cx="6" cy="6" r="5.3" fill="none" stroke="#333"/><ellipse cx="6" cy="6" rx="2.3" ry="5.3" fill="none" stroke="#333"/><path d="M.7 6h10.6M1.5 3.5h9M1.5 8.5h9" stroke="#333" stroke-width=".8"/></svg>
      www.thrivemetric.net
    </li>
    <li>
      <span class="social-dot"></span>
      /thrivemetric
    </li>
  </ul>

  <p class="tagline">Supporting individual growth<br>and&nbsp; organizational development.</p>

  <div class="person">
    <div class="person-name">Your Name</div>
    <div class="person-title">Title</div>
  </div>
</section>

<section class="card card-back" aria-label="Card back">
  <ul class="quote-list">
    <li class="quote">
      <span class="quote-dot"></span>
      <div class="quote-text">Try not to become a man of success, but rather a man of value.</div>
      <div class="quote-author">Arlen Whitcombe</div>
    </li>
    <li class="quote">
      <span class="quote-dot"></span>
      <div class="quote-text">The only constant is change.</div>
      <div class="quote-author">Doran Velis</div>
    </li>
    <li class="quote">
      <span class="quote-dot"></span>
      <div class="quote-text">We are what we repeatedly do. Excellence is not an act, it is a habit.</div>
      <div class="quote-author">Marcus Ellery</div>
    </li>
    <li class="quote">
      <span class="quote-dot"></span>
      <div class="quote-text">Simplicity is the ultimate sophistication.</div>
      <div class="quote-author">Lorenzo Valtieri</div>
    </li>
    <li class="quote">
      <span class="quote-dot"></span>
      <div class="quote-text">Life is not fair - get used to it.</div>
      <div class="quote-author">Ben Garrow</div>
    </li>
  </ul>
</section>

</body>
</html>
```